Flyer Vacation Gift Certificate

I need to create a beautiful flyer 8.5 x 11 PDF format flyer design. <br/><br/>Instructions:<br/>The flyer will really be a gift voucher for a las vegas vacation getaway. So must have a Las Vegas Theme exciting fun<br/><br/>The voucher should have two modules that will be editable. <br/>Must have a "Compliments Of" area and also must have an "Exclusively For" area<br/><br/>Keep in mind that this flyer will be printed so keep that in mind :)<br/><br/>Here the is the content for the vacation voucher:<br/><br/>There is no doubt that Las Vegas is one of the hottest travel destinations around the world. In fact, some people would even go as far as<br/>saying that perhaps it is THE hottest place to visit. Enjoy up to 4 nights of resort/casino accommodations in exciting Las Vegas, NV. Millions of people travel to this exciting city each year to enjoy its thrills. Thanks to the business you received this certificate from, now you can enjoy exciting Las Vegas, NV too!<br/><br/>Features:<br/>*Travel 7 Days A Week<br/>*Stay Your Choice Of Nights (1-4 Nights)<br/>*Good For Two Adults & Two Children<br/>*Pay Just The Taxes & Fees<br/>*Multiple Travel Date Requests Allowed<br/>*Fully Transferable To Another Person<br/>*Just A 30 Days Advance Notice Required<br/>*You Will Have 12 Months To Complete Travel After Redemption<br/><br/>HOW CAN WE DO THIS?<br/><br/>We contract with the world leading hotel chains and resorts to help them fill their otherwise empty rooms.<br/><br/>We help fill empty rooms which the hotels, resorts and cruise lines turn into additional revenue from other areas of their property and future bookings.<br/><br/>Hotels rarely experience full occupancy, yet they remain open, providing rooms and services at fixed costs. So when hotels give out their rooms by partnering with marketing companies like us, they might miss out on the room fee, but they already didn't have that in the first place, at least now they have the opportunity to gain a customer for their in-house restaurants, room service, their casinos, an extra day stay, future bookings, etc.<br/><br/>VIEW ALL THE DETAILS OF THIS SPECIAL OFFER AND REDEEM ONLINE AT <br/>WWW.TOPAZVOUCHERDESK.COM<br/><br/>Certificate ID # 47261-38504<br/>Expires 02/29/2020<br/><br/><br/>*terms and conditions apply see website for details<br/><br/>KEEP IN MIND THE EXAMPLES I AM UPLOADING ARE SIMPLY TO SHOW YOU THAT THEY CONTAIN THE "COMPLIMENTS OF" AND "EXCLUSIVELY FOR" ELEMENTS. THESE MUST BE INCLUDED IN NEW DESIGN. PLEASE ONLY USE THE CONTENT I PROVIDED IN BRIEF, DONT USE CONTENT FROM EXAMPLES.

Target Market(s)

CONSUMERS THAT HAVE BEEN REWARDED WITH A VACATION CERTIFICATE FOR DOING BUSINESS WITH A COMPANY.

COMPANIES USE THESE AS MARKETING INCENTIVES TO ATTRACT MORE CUSTOMERS AND TO REWARD LOYALTY, ETC.

Industry/Entity Type

Travel Industry

Colors

Designer to choose colors to be used in the design.

Requirements
Must have
• I need to create a beautiful flyer 8.5 x 11 PDF format flyer design.
• Instructions:
• The flyer will really be a gift voucher for a las vegas vacation getaway. So must have a Las Vegas Theme exciting fun
• The voucher should have two modules that will be editable.
• Must have a "Compliments Of" area and also must have an "Exclusively For" area
• Keep in mind that this flyer will be printed so keep that in mind :)
• Here the is the content for the vacation voucher:
• There is no doubt that Las Vegas is one of the hottest travel destinations around the world. In fact, some people would even go as far as
• saying that perhaps it is THE hottest place to visit. Enjoy up to 4 nights of resort/casino accommodations in exciting Las Vegas, NV. Millions of people travel to this exciting city each year to enjoy its thrills. Thanks to the business you received this certificate from, now you can enjoy exciting Las Vegas, NV too!
• Features:
• *Travel 7 Days A Week
• *Stay Your Choice Of Nights (1-4 Nights)
• *Good For Two Adults & Two Children
• *Pay Just The Taxes & Fees
• *Multiple Travel Date Requests Allowed
• *Fully Transferable To Another Person
• *Just A 30 Days Advance Notice Required
• *You Will Have 12 Months To Complete Travel After Redemption
• HOW CAN WE DO THIS?
• We contract with the world leading hotel chains and resorts to help them fill their otherwise empty rooms.
• We help fill empty rooms which the hotels, resorts and cruise lines turn into additional revenue from other areas of their property and future bookings.
• Hotels rarely experience full occupancy, yet they remain open, providing rooms and services at fixed costs. So when hotels give out their rooms by partnering with marketing companies like us, they might miss out on the room fee, but they already didn't have that in the first place, at least now they have the opportunity to gain a customer for their in-house restaurants, room service, their casinos, an extra day stay, future bookings, etc.
• VIEW ALL THE DETAILS OF THIS SPECIAL OFFER AND REDEEM ONLINE AT
• WWW.TOPAZVOUCHERDESK.COM
• Certificate ID # 47261-38504
• Expires 02/29/2020
• *terms and conditions apply see website for details
• KEEP IN MIND THE EXAMPLES I AM UPLOADING ARE SIMPLY TO SHOW YOU THAT THEY CONTAIN THE "COMPLIMENTS OF" AND "EXCLUSIVELY FOR" ELEMENTS. THESE MUST BE INCLUDED IN NEW DESIGN. PLEASE ONLY USE THE CONTENT I PROVIDED IN BRIEF, DONT USE CONTENT FROM EXAMPLES.
Nice to have
• EXCITING LAS VEGAS IMAGES THAT MAKE SOMEONE WANT TO GO THERE

```html
<!DOCTYPE html>
<html lang="en">
<head>
<meta charset="utf-8">
<title>Las Vegas Vacation Getaway Gift Voucher</title>
<link rel="stylesheet" href="https://fonts.googleapis.com/css2?family=Yellowtail&family=Ultra&family=Alfa+Slab+One&family=Open+Sans:wght@400;600&family=Montserrat:ital,wght@0,400;0,600;0,700;1,700&display=swap">
<style>
  :root{
    --stage:#e9e7e4;
    --paper:#f4f3f6;
    --navy:#1b2a7a;
    --red:#d7263d;
    --blue:#2a4bb8;
    --gold:#f2b01e;
    --yellow:#f4d21f;
    --ink:#2b2b33;
    --white:#ffffff;
  }
  *{box-sizing:border-box;margin:0;padding:0}
  html,body{width:1200px;height:800px;overflow:hidden;background:var(--stage)}
  .voucher{
    position:absolute;left:306px;top:20px;width:588px;height:760px;
    background:var(--paper);overflow:hidden;
    box-shadow:0 6px 24px rgba(0,0,0,.18);
    font-family:"Open Sans",sans-serif;color:var(--ink);
  }
  .voucher__art{position:absolute;left:0;top:0;width:588px;height:760px}
  .hero-photo{position:absolute;left:0;top:0;width:210px;height:250px}
  .photo{position:absolute;border-radius:50%;border:6px solid var(--red);box-shadow:0 2px 6px rgba(0,0,0,.25)}
  .photo--slots{left:218px;top:150px;width:140px;height:140px;z-index:3;
    background:radial-gradient(circle at 40% 40%,#b7456a,#5a2440 60%,#2b1a2e)}
  .photo--canal{left:360px;top:124px;width:170px;height:170px;z-index:2;
    background:linear-gradient(160deg,#6c9ad6 0%,#c9b79a 45%,#7b6a52 75%,#3d4a55)}
  .photo--party{left:360px;top:276px;width:196px;height:196px;z-index:3;
    background:radial-gradient(circle at 50% 45%,#c0603f,#5b2a2a 55%,#1f1622)}

  .title{position:absolute;right:34px;top:18px;text-align:right;z-index:4}
  .title__script{font-family:"Yellowtail",cursive;color:var(--gold);font-size:32px;line-height:1;margin-right:44px}
  .title__main{font-family:"Ultra",serif;color:var(--white);font-size:38px;line-height:1.05;letter-spacing:3px;font-weight:400}
  .title__sub{font-family:"Alfa Slab One",serif;color:var(--red);font-size:21px;line-height:1.1;margin-top:1px}

  .intro{position:absolute;left:30px;top:298px;width:310px;font-size:8.4px;line-height:1.4}

  .features__heading{position:absolute;left:30px;top:384px;font-family:"Montserrat",sans-serif;
    font-style:italic;font-weight:700;font-size:14.5px;color:var(--ink)}
  .checklist{list-style:none;position:absolute;font-size:8.4px;line-height:1.3}
  .checklist li{position:relative;padding-left:14px;margin-bottom:3px}
  .checklist li::before{content:"";position:absolute;left:0;top:1px;width:8px;height:8px;
    border:1.3px solid var(--red);border-radius:1px}
  .checklist li::after{content:"";position:absolute;left:2px;top:1.5px;width:3px;height:5px;
    border:solid var(--red);border-width:0 1.5px 1.5px 0;transform:rotate(40deg)}
  .checklist--a{left:30px;top:406px;width:190px}
  .checklist--b{left:222px;top:390px;width:125px}

  .how__heading{position:absolute;left:30px;top:484px;font-family:"Montserrat",sans-serif;
    font-style:italic;font-weight:700;font-size:14px;letter-spacing:.5px}
  .how__list{list-style:none;position:absolute;left:30px;top:504px;width:340px;font-size:8.2px;line-height:1.35}
  .how__list li{position:relative;padding-left:13px;margin-bottom:4px}
  .how__list li::before{content:"";position:absolute;left:0;top:3px;width:6px;height:6px;border-radius:50%;background:var(--red)}

  .fields{position:absolute;left:30px;top:630px;width:240px;font-family:"Montserrat",sans-serif;
    font-weight:700;font-size:9px;letter-spacing:.4px}
  .fields__row{display:flex;align-items:flex-end;margin-bottom:8px}
  .fields__line{flex:1;border-bottom:1.4px dotted var(--ink);margin-left:6px;height:9px}

  .cert{position:absolute;left:418px;top:612px;font-family:"Montserrat",sans-serif;font-size:11px;line-height:1.55;z-index:4;color:var(--white)}
  .cert__label{color:var(--yellow);font-weight:700}
  .redeem{position:absolute;left:30px;top:714px;font-family:"Montserrat",sans-serif;color:var(--white);
    font-size:12.5px;line-height:1.35;z-index:4}
  .redeem__url{color:var(--yellow)}
</style>
</head>
<body>
<main class="voucher">
  <svg class="voucher__art" viewBox="0 0 588 760" aria-hidden="true">
    <defs>
      <linearGradient id="night" x1="0" y1="0" x2="1" y2="1">
        <stop offset="0" stop-color="#0b0610"/>
        <stop offset=".55" stop-color="#3a1852"/>
        <stop offset="1" stop-color="#7a2a6a"/>
      </linearGradient>
    </defs>
    <path d="M0,0H588V230C420,205 260,205 160,240C95,262 45,276 0,278Z" fill="url(#night)"/>
    <path d="M0,278C45,276 95,262 160,240C260,205 420,205 588,230" fill="none" stroke="#d7263d" stroke-width="6"/>
    <path d="M0,286C45,284 95,270 160,248C260,213 420,213 588,238" fill="none" stroke="#2a4bb8" stroke-width="4"/>
    <path d="M0,705C170,703 310,680 400,615C470,555 540,480 588,440V760H0Z" fill="#1b2a7a"/>
    <path d="M0,699C170,697 310,674 398,609C468,549 538,474 588,434" fill="none" stroke="#d7263d" stroke-width="5"/>
  </svg>

  <div class="hero-photo" role="img" aria-label="Night photo of the Las Vegas Strip with the Welcome to Las Vegas sign"></div>
  <div class="photo photo--canal" role="img" aria-label="Photo of a Venetian-style hotel canal with a gondola"></div>
  <div class="photo photo--slots" role="img" aria-label="Photo of friends playing a slot machine"></div>
  <div class="photo photo--party" role="img" aria-label="Photo of a cheering group at a casino table with flying chips"></div>

  <header class="title">
    <p class="title__script">Gift voucher</p>
    <h1 class="title__main">LAS VEGAS</h1>
    <p class="title__sub">vacation getaway</p>
  </header>

  <p class="intro">There is no doubt that Las Vegas is one of the hottest travel destinations around the world. In fact, some people would even go as far as saying that perhaps it is THE hottest place to visit. Enjoy up to 4 nights of resort/ casino accommodations in exciting Las Vegas, NV. Millions of people travel to this exciting city each year to enjoy its thrills. Thanks to the business you received this certificate from, now you can enjoy exciting Las Vegas, NV too!</p>

  <h2 class="features__heading">Features :</h2>
  <ul class="checklist checklist--a">
    <li>Travel 7 Days A Week</li>
    <li>Stay Your Choice Of Nights (1-4 Nights)</li>
    <li>Good For Two Adults &amp; Two Children</li>
    <li>Pay Just The Taxes &amp; Fees</li>
    <li>Multiple Travel Date Requests Allowed</li>
  </ul>
  <ul class="checklist checklist--b">
    <li>Fully Transferable To Another Person</li>
    <li>Just A 30 Days Advance Notice Required</li>
    <li>You Will Have 12 Months To Complete Travel After Redemption</li>
  </ul>

  <h2 class="how__heading">HOW CAN WE DO THIS ?</h2>
  <ul class="how__list">
    <li>We contract with the world leading hotel chains and resorts to help them fill their otherwise empty rooms.</li>
    <li>We help fill empty rooms which the hotels, resorts and cruise lines turn into additional revenue from other areas of their property and future bookings.</li>
    <li>Hotels rarely experience full occupancy, yet they remain open, providing rooms and services at fixed costs. So when hotels give out their rooms by partnering with marketing companies like us, they might miss out on the room fee, but they already didn't have that in the first place, at least now they have the opportunity to gain a customer for their in-house restaurants, room service, their casinos, an extra day stay, future bookings, etc.</li>
  </ul>

  <div class="fields">
    <div class="fields__row"><span>EXCLUSIVELY FOR :</span><span class="fields__line"></span></div>
    <div class="fields__row"><span>COMPLIMENTS OF :</span><span class="fields__line"></span></div>
  </div>

  <div class="cert">
    <p><span class="cert__label">Expires</span> 02/29/2020</p>
    <p><span class="cert__label">Certificate ID</span> # 47261-38504</p>
  </div>

  <p class="redeem">View all the details of this special offer<br>&amp; redeem online at <span class="redeem__url">www.TopazVoucherDesk.Com</span></p>
</main>
</body>
</html>
```